Cocktail Menu

I need a drink menu that will be prited on a heavy weight card designed. I want it to be something differtent that guests will look at then order a drink. The card will be on the bar or given to customers at tables. This is for a upscale restaurant in Northern Virginia. The website is www.BriarmossRestaruant.com if you want to see pictures. I will attach rthe drinks and our logo. I need something really attractive and different. It can be larger then a postcard but not stanadard paper sizes.
Updates

The menu can be larger then a postcard and the front and back can be used if needed.

Industry/Entity Type

Restaurant

```html
<!DOCTYPE html>
<html lang="en">
<head>
<meta charset="utf-8">
<title>Drink Menu</title>
<link rel="stylesheet" href="https://fonts.googleapis.com/css2?family=Alegreya:wght@400;500&display=swap">
<style>
  :root {
    --bg-deep: #1c0913;
    --bg-glow: #2e1320;
    --frame-line: #a88680;
    --heading-gold: #eaae5c;
    --item-coral: #de7049;
    --price-white: #f6eee6;
  }
  * { margin: 0; padding: 0; box-sizing: border-box; }
  html, body { width: 900px; height: 1200px; overflow: hidden; background: var(--bg-deep); }
  .menu-card {
    position: relative;
    width: 900px;
    height: 1200px;
    overflow: hidden;
    font-family: "Alegreya", Georgia, serif;
    text-align: center;
  }
  .backdrop {
    position: absolute;
    inset: 0;
    background:
      radial-gradient(ellipse at 30% 20%, rgba(90,50,70,0.35), transparent 55%),
      radial-gradient(ellipse at 75% 70%, rgba(80,45,65,0.3), transparent 55%),
      linear-gradient(180deg, var(--bg-glow), var(--bg-deep));
  }
  .frame { position: absolute; inset: 0; }
  .menu-content { position: absolute; left: 0; right: 0; top: 68px; }
  .section-title {
    font-weight: 500;
    font-size: 64px;
    line-height: 70px;
    height: 70px;
    color: var(--heading-gold);
  }
  .section-title.cocktails { margin-top: 12px; }
  .drink-list { list-style: none; }
  .drink-line {
    display: block;
    height: 41.2px;
    font-size: 24px;
    line-height: 41.2px;
    color: var(--item-coral);
    white-space: nowrap;
  }
  .price {
    font-size: 19px;
    line-height: 1;
    color: var(--price-white);
  }
</style>
</head>
<body>
<main class="menu-card">
  <div class="backdrop" role="img" aria-label="Soft blurred bokeh lights on a deep wine background"></div>
  <svg class="frame" width="900" height="1200" viewBox="0 0 900 1200" aria-hidden="true">
    <path d="M150 32 H750 A32 32 0 0 0 782 64 Q790 88 832 88 V1112 Q790 1112 782 1136 A32 32 0 0 0 750 1168 H150 A32 32 0 0 0 118 1136 Q110 1112 68 1112 V88 Q110 88 118 64 A32 32 0 0 0 150 32 Z"
      fill="none" stroke="var(--frame-line)" stroke-width="3"/>
  </svg>

  <div class="menu-content">
    <section class="menu-section">
      <h1 class="section-title">Martinis</h1>
      <ul class="drink-list">
        <li>
          <span class="drink-line">The Old Banker-</span>
          <span class="drink-line">Iced Cold Tamsin’s Handmade Vodka,</span>
          <span class="drink-line">Blue Cheese Olives <span class="price">$12</span></span>
        </li>
        <li>
          <span class="drink-line">French Kiss Martini- Volka Raspberry,</span>
          <span class="drink-line">Chantelle, Pineapple <span class="price">$10</span></span>
        </li>
        <li>
          <span class="drink-line">Honey Apple Nip Martini- Honey Jed Darrow’s,</span>
          <span class="drink-line">Gander Vodka,Cider,</span>
          <span class="drink-line">Fall Spices and touch of Honey <span class="price">$11</span></span>
        </li>
        <li>
          <span class="drink-line">Italiano Lemon Drop- Volka Citrus Vodka,</span>
          <span class="drink-line">Lemoncello, Crystallized Rim, Lemon Twist <span class="price">$11</span></span>
        </li>
        <li>
          <span class="drink-line">Cheng Jiang Martini- Barrado O,</span>
          <span class="drink-line">Calder Ginger, Tivella, OJ <span class="price">$11</span></span>
        </li>
        <li>
          <span class="drink-line">Perfect Pear- Absolon Pear Vodka, St. Gervais,</span>
          <span class="drink-line">Peach Schnapps, Apple Juice <span class="price">$10</span></span>
        </li>
      </ul>
    </section>

    <section class="menu-section">
      <h2 class="section-title cocktails">Cocktails</h2>
      <ul class="drink-list">
        <li>
          <span class="drink-line">The Tipsy Judge- Prosecco, St. Gervais,</span>
          <span class="drink-line">Gin, and Japanese Yuzu, and a Strawberry <span class="price">$12</span></span>
        </li>
        <li>
          <span class="drink-line">Tart Love- Bramwell Gin, Cambrino,</span>
          <span class="drink-line">St. Gervaise, Pineapple <span class="price">$10</span></span>
        </li>
        <li>
          <span class="drink-line">I Love Lottie- Volka Vanilla, Chantelle,</span>
          <span class="drink-line">Pineapple Juice, Champagne <span class="price">$10</span></span>
        </li>
        <li>
          <span class="drink-line">Brazilian Fresh- 12 Reed Rum,</span>
          <span class="drink-line">Fresh Lime, and Grapefruit <span class="price">$12</span></span>
        </li>
      </ul>
    </section>
  </div>
</main>
</body>
</html>
```